Banner Ad Design Project

I place ads in Clickreach and also get traffic from sites like http://www.holisticcarelist.com.au/ to offer our free meditation CD and report at http://quietpathstudio.com.au/get-the-free-meditation-cd
We need new designs to improve this campaign.
Target Market(s)
40+ year old women, looking for personal growth or help with stress, depression, anxiety, sleep problems, health issues, memory/concentration issues
Industry/Entity Type
Campaign

```html
<!DOCTYPE html>
<html lang="en">
<head>
<meta charset="utf-8">
<title>Quiet Path – Banner Set</title>
<link rel="stylesheet" href="https://fonts.googleapis.com/css2?family=Arimo:wght@700&family=Roboto+Condensed:wght@400;700&display=swap">
<style>
  :root {
    --bg: #1d1d1d;
    --green-light: #8fc43c;
    --green-mid: #6a9f2a;
    --green-deep: #4a7a1c;
    --forest: #10250f;
    --paper: #ffffff;
    --ink: #161616;
    --gold: #f7b814;
    --text-light: #f4f7ee;
    --disc: #9fb6d8;
    --disc-edge: #5d7fb5;
    --photo-light: #eef0ea;
    --photo-shade: #c9cfc0;
  }
  * { box-sizing: border-box; margin: 0; padding: 0; }
  html, body { width: 1200px; height: 1200px; overflow: hidden; background: var(--bg); }
  .canvas { position: relative; width: 1200px; height: 1200px; background: var(--bg); }

  .banner {
    position: absolute; overflow: hidden;
    background: linear-gradient(180deg, var(--green-light) 0%, var(--green-mid) 60%, var(--green-deep) 100%);
    font-family: "Arimo", Arial, sans-serif; color: var(--text-light);
  }
  .banner svg.shapes { position: absolute; inset: 0; width: 100%; height: 100%; }
  .banner > * { position: absolute; }
  .brand { color: var(--ink); font-family: "Arimo", Arial, sans-serif; font-weight: 700; line-height: 1; white-space: nowrap; }
  .line { white-space: nowrap; line-height: 1; font-weight: 700; text-shadow: 2px 2px 3px rgba(0,0,0,.55); }
  .condensed { font-family: "Roboto Condensed", "Arial Narrow", sans-serif; font-weight: 400; letter-spacing: -0.4px; }
  .price { color: var(--gold); font-weight: 700; }
  .disc {
    border-radius: 50%;
    background: radial-gradient(circle at 50% 50%, #e8eef6 0 14%, var(--disc) 15% 70%, var(--disc-edge) 100%);
  }
  .photo {
    border-radius: 40% 40% 20% 20%;
    background: radial-gradient(ellipse at 50% 45%, var(--photo-light) 0%, var(--photo-shade) 70%, rgba(201,207,192,0) 100%);
  }

  .sky { left: 92px; top: 46px; width: 224px; height: 840px; }
  .rect { left: 480px; top: 84px; width: 504px; height: 422px; }
  .slim { left: 424px; top: 562px; width: 632px; height: 82px; }
  .wide { left: 377px; top: 720px; width: 741px; height: 133px; }
</style>
</head>
<body>
<main class="canvas">

  <!-- Skyscraper 224 x 840 -->
  <section class="banner sky" aria-label="Quiet Path skyscraper banner">
    <svg class="shapes" viewBox="0 0 224 840" preserveAspectRatio="none" aria-hidden="true">
      <path d="M0 0 H224 V108 Q150 150 0 130 Z" fill="var(--forest)" opacity=".35"/>
      <path d="M0 0 H224 V104 Q150 140 0 124 Z" fill="var(--paper)"/>
      <path d="M0 840 V660 Q90 610 224 648 V840 Z" fill="var(--forest)"/>
    </svg>
    <div class="brand" style="left:12px;top:30px;font-size:36px;">Quiet</div>
    <div class="brand" style="left:50px;top:72px;font-size:36px;">Path</div>
    <div class="disc" role="img" aria-label="Meditation CD disc artwork" style="left:54px;top:156px;width:108px;height:108px;"></div>
    <div class="line condensed" style="left:0;width:224px;text-align:center;top:273px;font-size:24px;">FREE Meditation CD</div>
    <div class="line condensed" style="left:0;width:224px;text-align:center;top:309px;font-size:24px;">and Special Report</div>
    <div class="photo" role="img" aria-label="Photo of a woman in white meditating cross-legged" style="left:28px;top:342px;width:168px;height:196px;"></div>
    <div class="line condensed" style="left:0;width:224px;text-align:center;top:544px;font-size:25px;">How to Meditate</div>
    <div class="line condensed" style="left:0;width:224px;text-align:center;top:583px;font-size:21px;">Deeper Than a Zen Monk!</div>
    <div class="line" style="left:0;width:224px;text-align:center;top:664px;font-size:27px;">valued</div>
    <div class="line" style="left:8px;width:224px;text-align:center;top:707px;font-size:34px;">at</div>
    <div class="line price" style="left:8px;width:224px;text-align:center;top:762px;font-size:62px;">$37</div>
  </section>

  <!-- Rectangle 504 x 422 -->
  <section class="banner rect" aria-label="Quiet Path rectangle banner">
    <svg class="shapes" viewBox="0 0 504 422" preserveAspectRatio="none" aria-hidden="true">
      <path d="M0 0 H300 Q340 30 318 70 Q290 118 150 116 Q60 114 0 98 Z" fill="var(--forest)" opacity=".35"/>
      <path d="M0 0 H290 Q330 28 308 66 Q282 110 150 110 Q60 108 0 92 Z" fill="var(--paper)"/>
      <path d="M110 422 Q170 330 330 310 Q430 300 504 300 V422 Z" fill="var(--forest)"/>
    </svg>
    <div class="brand" style="left:38px;top:16px;font-size:38px;">Quiet</div>
    <div class="brand" style="left:48px;top:60px;font-size:38px;">Path</div>
    <div class="disc" role="img" aria-label="Meditation CD disc artwork" style="left:348px;top:20px;width:124px;height:124px;"></div>
    <div class="line" style="left:20px;top:142px;font-size:25px;">FREE Meditation CD</div>
    <div class="line" style="left:27px;top:174px;font-size:25px;">and Special Report</div>
    <div class="photo" role="img" aria-label="Photo of a woman in white meditating cross-legged" style="left:10px;top:208px;width:134px;height:180px;"></div>
    <div class="line" style="left:174px;width:260px;text-align:center;top:218px;font-size:30px;">How to Meditate</div>
    <div class="line" style="left:152px;top:256px;font-size:26px;">Deeper Than a Zen Monk!</div>
    <div class="line" style="left:205px;top:354px;font-size:36px;">Value at <span class="price" style="font-size:56px;">$37</span></div>
  </section>

  <!-- Slim leaderboard 632 x 82 -->
  <section class="banner slim" aria-label="Quiet Path slim leaderboard banner">
    <svg class="shapes" viewBox="0 0 632 82" preserveAspectRatio="none" aria-hidden="true">
      <path d="M0 0 H160 Q180 22 168 44 Q150 68 70 66 Q30 64 0 58 Z" fill="var(--paper)"/>
      <path d="M370 82 Q420 30 560 10 Q600 4 632 0 V82 Z" fill="var(--forest)"/>
    </svg>
    <div class="brand" style="left:12px;top:4px;font-size:22px;">Quiet</div>
    <div class="brand" style="left:20px;top:32px;font-size:22px;">Path</div>
    <div class="line condensed" style="left:182px;top:5px;font-size:16px;">FREE Meditation CDand Special Report</div>
    <div class="line" style="left:198px;top:30px;font-size:17px;">How to Meditate</div>
    <div class="line" style="left:184px;top:53px;font-size:14px;">Deeper Than a Zen Monk!</div>
    <div class="line" style="left:452px;top:34px;font-size:19px;">Value at <span class="price" style="font-size:34px;">$37</span></div>
  </section>

  <!-- Wide leaderboard 741 x 133 -->
  <section class="banner wide" aria-label="Quiet Path wide leaderboard banner">
    <svg class="shapes" viewBox="0 0 741 133" preserveAspectRatio="none" aria-hidden="true">
      <path d="M0 0 H234 Q252 40 228 70 Q200 96 110 94 Q40 92 0 86 Z" fill="var(--paper)"/>
      <path d="M430 133 Q490 60 620 46 Q690 40 741 40 V133 Z" fill="var(--forest)"/>
    </svg>
    <div class="brand" style="left:14px;top:14px;font-size:30px;">Quiet</div>
    <div class="brand" style="left:23px;top:48px;font-size:30px;">Path</div>
    <div class="line condensed" style="left:272px;top:10px;font-size:26px;">FREE Meditation CDand Special Report</div>
    <div class="disc" role="img" aria-label="Small meditation CD disc artwork" style="left:681px;top:4px;width:40px;height:40px;"></div>
    <div class="line" style="left:241px;top:64px;font-size:24px;">How to Meditate</div>
    <div class="line" style="left:223px;top:91px;font-size:20px;">Deeper Than a Zen Monk!</div>
    <div class="line" style="left:519px;top:80px;font-size:23px;">Valued at <span class="price" style="font-size:54px;">$37</span></div>
  </section>

</main>
</body>
</html>
```